July 2022 Industrial Manufacturer Product Expo Mexico City

We manufacture large screws and fastners for large Mining equipment, Trains, large ships, airplanes, wind turbines, and so on. We also do custom work base on the customer needs. No matter the size we can make it.
We have a Expo coming up with companies all over the world. We have to stand out we are a family own business so our customer service will be above and beyond anyone can provide. We do not have a sales force to push our products and services we provide one on one service.
Plus@!! I'm looking for anything that you designers can come up with if it was your company to put on a business card, plus i want to do a 1 or 2 sided pamphlet, and then a website. We make Speciality Bolts for large mining equipment these bolts can be 3 to 4 foot long!!! Plus fasteners, Nuts, washers, any, size, strengths, special materials, we offer more of a ono on one customer service, We are a small company, family own, but can fulfill any type of orders. We can also provide special time lines for emergency orders. "We keep the machines running we here at RWK don't believe in down time" We want to hear any slogan based on our company to stand out.
Thanks i really appreciate all your work and options that we have to pick on. Plus just a thought we could possibly want to entertain a experience Marketing internet help maybe a employment possibility. Thanks
Updates

I need 2 cards one in Spanish and English Like the steel back ground maybe send me in some bright red and blue writing Same with the Black cards Please remove the word Military The logo RWK maybe integrate a picture of a Bolt 🔩 Thank you

Still looking for I need 2 cards one in Spanish and English Like the steel back ground maybe send me in some bright red and blue writing Same with the Black cards try bright writing Please remove the word Military The logo RWK maybe integrate a picture of a Bolt 🔩 Plus will need the company to make a brochure and website next Thank you

Target Market(s)

Large Mining, Ship, Train, Green Energy, OPRE, and Government equipment. Throughout the World

Industry/Entity Type

We can Custom Manufacture any type of Fastners for Mining equipment, Trains, Ships, Green energy, Governments, or military projects. wind turbines,

Contact Information for Business Card

I attached the name and contact info that's on a card, plus the Company Logo. Would like industrial looking background with Bright Colors that will stand out!! If we can insert somewhere maybe on back that we "Custom Manufacture Any Size or Quantity Fastners for Large Mining Equipment, Trains, Ships, Green Energy Equipment or Government Projects

Font styles to use
Other font styles liked:
• You Pick, has to be bold, colorful standout, Professional looking Beable to read it.

Colors

Designer to choose colors to be used in the design.

Requirements
Must have
• Need in Spanish and English TO STANDOUT FROM THE REST OF THE EXPO!! See Business card details, Rounded corners
Nice to have
• Can i see some of the darker cards with Bright Red and Blue letters I like to see the different type of card material, heavy thickness, plastic, transparent, Metal types, Bright Colors, I saw like Raised letters like on the logo.

```html
<!DOCTYPE html>
<html lang="es">
<head>
<meta charset="utf-8">
<title>RWK – Tarjetas de presentación</title>
<link href="https://fonts.googleapis.com/css2?family=Source+Sans+3:wght@400;600;700&display=swap" rel="stylesheet">
<style>
  :root {
    --backdrop: #121214;
    --card: #26272b;
    --card-deep: #1f2023;
    --edge-blue: #0a8fe0;
    --edge-navy: #0b2d8c;
    --name-blue: #1b8fd8;
    --rule-navy: #1c3a9c;
    --mark-grey: #6b6c70;
    --text-white: #f2f3f5;
    --bright-red: #ff2a2a;
  }
  * { box-sizing: border-box; margin: 0; padding: 0; }
  html, body {
    width: 1200px; height: 820px; overflow: hidden;
    background: var(--backdrop);
    font-family: "Source Sans 3", "Myriad Pro", sans-serif;
  }
  .sheet {
    width: 1200px; height: 820px;
    display: flex; align-items: center; justify-content: center; gap: 40px;
  }
  .card {
    position: relative;
    width: 550px; height: 314px;
    background: linear-gradient(160deg, var(--card) 0%, var(--card-deep) 100%);
    border-radius: 8px;
    border-left: 3px solid var(--edge-navy);
    border-bottom: 3px solid var(--edge-blue);
    box-shadow: 0 0 0 1px rgba(10,143,224,0.25);
    overflow: hidden;
  }
  .brand {
    position: absolute;
    font-weight: 700;
    letter-spacing: 0.12em;
    color: var(--mark-grey);
    display: flex; align-items: center; gap: 12px;
    line-height: 1;
  }
  .brand-dot {
    width: 14px; height: 14px; border-radius: 50%;
    background: var(--name-blue);
  }
  .card-front .brand { left: 250px; top: 58px; font-size: 64px; color: var(--name-blue); }
  .holder-name {
    position: absolute; left: 36px; top: 178px;
    font-size: 22px; font-weight: 400; color: var(--name-blue);
  }
  .name-rule {
    position: absolute; left: 36px; right: 30px; top: 212px;
    height: 1px; background: var(--rule-navy);
  }
  .contact {
    position: absolute; left: 36px; top: 222px;
    color: var(--text-white); font-size: 15px; line-height: 1.35;
  }
  .contact .phones { display: flex; align-items: center; gap: 8px; margin-top: 6px; font-size: 16px; }
  .contact svg { width: 15px; height: 15px; fill: var(--name-blue); flex: none; }
  .card-back .brand { left: 50%; top: 86px; transform: translateX(-50%); font-size: 72px; }
  .tagline {
    position: absolute; left: 30px; right: 30px; top: 190px;
    text-align: center; color: var(--bright-red);
    font-size: 16px; font-weight: 600; line-height: 1.4;
  }
</style>
</head>
<body>
<main class="sheet">
  <section class="card card-front" aria-label="Frente de la tarjeta">
    <div class="brand"><span class="brand-dot"></span>RWK</div>
    <p class="holder-name">Lic. Daniela Marisol Vega Ruiz</p>
    <div class="name-rule"></div>
    <div class="contact">
      <p>Cotizaciones en</p>
      <p>rwk.cotizaciones@correo.mx</p>
      <p class="phones">
        <svg viewBox="0 0 24 24" aria-hidden="true"><path d="M6.6 10.8a15.1 15.1 0 0 0 6.6 6.6l2.2-2.2c.3-.3.7-.4 1-.2 1.1.4 2.3.6 3.6.6.6 0 1 .4 1 1V20c0 .6-.4 1-1 1A17 17 0 0 1 3 4c0-.6.4-1 1-1h3.5c.6 0 1 .4 1 1 0 1.3.2 2.5.6 3.6.1.3 0 .7-.2 1z"/></svg>
        <span>5550193412</span>
        <svg viewBox="0 0 24 24" aria-hidden="true"><path d="M7 1h10a2 2 0 0 1 2 2v18a2 2 0 0 1-2 2H7a2 2 0 0 1-2-2V3a2 2 0 0 1 2-2zm0 3v14h10V4zm5 15.5a1 1 0 1 0 0 2 1 1 0 0 0 0-2z"/></svg>
        <span>5550287716</span>
      </p>
    </div>
  </section>

  <section class="card card-back" aria-label="Reverso de la tarjeta">
    <div class="brand">RWK</div>
    <p class="tagline">Custom Manufacture Any Size or Quantity Fastners for Large<br>Mining Equipment, Trains, Ships, Green Energy Equipment<br>or Government Projects</p>
  </section>
</main>
</body>
</html>
```